New more attractive design for an old tired look that is high tech but inviting

Need a more modern eye catching design. We are and I/T and MSP and we need a new look. Need a call to action on each page. Needs to be in WordPress. Existing site is quorbelna.com. Needs to work on phones and tablets. The default home page should present us as an MSP/MSSP and direct the viewer to our services we offer.
Updates

Current deadline assigned at project inception has passed before project started

Need extra days to review

Target Market(s)

Our target market is other businesses. We do not target residential customers.

Industry/Entity Type

Business to Business oriented

Coding

Coded - Design and coding required

Number of Pages Required

5+ page

Font styles to use
Sans Serif

Requirements
Must have
• Must have a current relevant design with a call to action on each page.
Nice to have
• Dark background high tech look with people to make it attractive

```html
<!DOCTYPE html>
<html lang="en">
<head>
<meta charset="utf-8">
<title>Quorbelna Solutions – Data Center Services</title>
<link href="https://fonts.googleapis.com/css2?family=Poppins:wght@300;400;500;600;700&display=swap" rel="stylesheet">
<style>
:root{
  --red:#c8262e;
  --slate:#2e3f49;
  --ink:#1d1d1d;
  --muted:#5c5c5c;
  --light:#f6f6f6;
  --pink:#fbe2e4;
  --white:#ffffff;
  --field:rgba(70,80,88,.72);
}
*{box-sizing:border-box;margin:0;padding:0}
html,body{width:1200px;height:3188px;overflow:hidden}
body{font-family:'Poppins',sans-serif;color:var(--ink);background:var(--white);position:relative}
.abs{position:absolute}
.brand{font-family:'Poppins',sans-serif;font-weight:600;color:var(--white);font-size:26px;line-height:1.1;white-space:nowrap}
.brand small{font-size:26px;font-weight:600;display:block;padding-left:48px}
.btn{position:absolute;display:flex;align-items:center;justify-content:center;gap:12px;background:var(--red);color:var(--white);font-weight:600;font-size:15px;text-decoration:none}
.btn-bar{position:absolute;background:var(--red);width:6px}
.accent-rule{position:absolute;height:2px;background:var(--red)}

/* header + hero */
.hero{position:absolute;left:0;top:0;width:1200px;height:674px;background:linear-gradient(100deg,#0b1724 0%,#142536 40%,#1d3043 70%,#0f1a26 100%)}
.hero-photo{position:absolute;inset:0;background:radial-gradient(ellipse at 78% 45%,rgba(95,120,150,.45),transparent 55%),radial-gradient(ellipse at 30% 30%,rgba(40,90,140,.35),transparent 50%)}
.site-header{position:absolute;left:0;top:0;width:1200px;height:82px;border-bottom:1px solid rgba(255,255,255,.15)}
.site-header .brand{position:absolute;left:62px;top:13px;font-size:22px}
.site-header .brand small{font-size:22px;padding-left:40px}
.nav a{position:absolute;top:33px;color:var(--white);font-size:15px;text-decoration:none}
.nav a.active::after{content:"";position:absolute;left:-2px;right:-2px;top:47px;height:2px;background:var(--white)}
.hero-title{position:absolute;left:58px;top:232px;color:var(--white);font-size:59px;font-weight:700;line-height:1}
.hero-sub{position:absolute;left:204px;top:310px;color:var(--white);font-size:59px;font-weight:300;line-height:1}
.hero-text{position:absolute;left:62px;top:387px;width:460px;color:var(--white);font-size:13.5px;line-height:23px}

/* features */
.features{position:absolute;left:0;top:674px;width:1200px;height:499px;background:var(--light)}
.feat-box{position:absolute;width:68px;height:68px;background:var(--slate);display:flex;align-items:center;justify-content:center}
.feat-box.red{background:var(--red)}
.feat h3{font-size:18px;font-weight:600;color:var(--ink)}
.feat p{font-size:13px;line-height:19.7px;color:var(--muted);margin-top:6px}
.center-brand{color:var(--slate);font-size:38px}
.center-brand small{font-size:30px;font-weight:600;padding-left:70px}

/* about */
.about-frame{position:absolute;left:58px;top:1247px;width:483px;height:414px;border:1.5px solid var(--red)}
.about-photo{position:absolute;left:83px;top:1270px;width:487px;height:412px;background:linear-gradient(135deg,#d8dde2,#b9c2ca 45%,#6f7c86 80%,#3f4a53)}
.about-copy{position:absolute;left:616px;top:1284px;width:492px}
.eyebrow{font-size:19px;color:var(--ink)}
.section-title{font-size:30px;font-weight:600;color:var(--slate);line-height:1.2}
.about-copy p{font-size:13px;line-height:19.7px;color:var(--muted);margin-top:10px}

/* services */
.services-title{position:absolute;left:0;width:1200px;top:1754px;text-align:center}
.svc{position:absolute;width:280px;text-align:center}
.svc-icon{width:75px;height:75px;margin:0 auto;background:var(--pink);display:flex;align-items:center;justify-content:center}
.svc h3{font-size:18px;font-weight:600;color:var(--slate);line-height:21px;margin-top:17px}
.svc p{font-size:13px;line-height:20px;color:var(--muted);margin-top:10px}
.svc-rule{position:absolute;left:79px;top:2055px;width:1042px;height:1px;background:#e3e3e3}

/* contact */
.contact{position:absolute;left:0;top:2344px;width:1200px;height:467px;background:linear-gradient(100deg,#0d1620 0%,#1a2a38 45%,#162230 100%)}
.contact h2{position:absolute;color:var(--white);font-size:30px;font-weight:600}
.contact-divider{position:absolute;left:366px;top:78px;width:1px;height:306px;background:rgba(255,255,255,.25)}
.c-item{position:absolute;left:62px;color:var(--white)}
.c-item h4{font-size:15px;font-weight:600;display:flex;align-items:center;gap:16px}
.c-item p{font-size:13px;line-height:21px;margin-top:8px}
.field{position:absolute;background:var(--field);border:1px solid rgba(255,255,255,.05);color:var(--white);font-size:13px;padding:11px 15px}

/* footer */
.footer{position:absolute;left:0;top:2811px;width:1200px;height:377px;background:var(--slate);color:var(--white)}
.footer .brand{position:absolute;left:62px;top:44px;font-size:26px}
.social{position:absolute;top:146px;width:40px;height:40px;border:1.5px solid var(--white)}
.f-col{position:absolute}
.f-col h4{font-size:18px;font-weight:600}
.f-col a{display:block;color:var(--white);font-size:13px;text-decoration:none;line-height:24px}
.f-contact{position:absolute;left:882px}
.f-icon{position:absolute;left:0;width:40px;height:40px;border:1.5px solid var(--white);display:flex;align-items:center;justify-content:center}
.f-text{position:absolute;left:67px;width:190px}
.f-text h5{font-size:15px;font-weight:600}
.f-text p{font-size:13px;line-height:21px;margin-top:3px}
.f-rule{position:absolute;left:58px;top:329px;width:1084px;height:1px;background:rgba(255,255,255,.25)}
.copyright{position:absolute;left:0;width:1200px;top:343px;text-align:center;font-size:13px}
</style>
</head>
<body>

<section class="hero">
  <div class="hero-photo" role="img" aria-label="Engineer typing at a keyboard in a dim data center with server racks behind him"></div>
  <header class="site-header">
    <div class="brand">Quorbelna<small>Solutions</small></div>
    <nav class="nav">
      <a class="active" href="#" style="left:568px">Home</a>
      <a href="#" style="left:644px">About Us</a>
      <a href="#" style="left:742px">Services</a>
      <a href="#" style="left:835px">Contact Us</a>
    </nav>
    <a class="btn" href="#" style="left:952px;top:22px;width:175px;height:40px">
      <svg width="20" height="20" viewBox="0 0 24 24"><path fill="#fff" d="M6.6 10.8a15.1 15.1 0 0 0 6.6 6.6l2.2-2.2a1 1 0 0 1 1-.25 11.4 11.4 0 0 0 3.6.57 1 1 0 0 1 1 1V20a1 1 0 0 1-1 1A17 17 0 0 1 3 4a1 1 0 0 1 1-1h3.5a1 1 0 0 1 1 1c0 1.25.2 2.45.57 3.57a1 1 0 0 1-.25 1z"/></svg>
      555-014-2279</a>
    <span class="btn-bar" style="left:1133px;top:22px;height:40px"></span>
  </header>
  <h1 class="hero-title">Data Center</h1>
  <span class="accent-rule" style="left:60px;top:306px;width:238px"></span>
  <div class="hero-sub">Services</div>
  <p class="hero-text">We offer colocation, virtualization, storage as a service and disaster recovery out of our own enterprise-grade data center.</p>
  <a class="btn" href="#" style="left:60px;top:460px;width:175px;height:40px">
    <svg width="20" height="20" viewBox="0 0 24 24"><path fill="#fff" d="M6.6 10.8a15.1 15.1 0 0 0 6.6 6.6l2.2-2.2a1 1 0 0 1 1-.25 11.4 11.4 0 0 0 3.6.57 1 1 0 0 1 1 1V20a1 1 0 0 1-1 1A17 17 0 0 1 3 4a1 1 0 0 1 1-1h3.5a1 1 0 0 1 1 1c0 1.25.2 2.45.57 3.57a1 1 0 0 1-.25 1z"/></svg>
    555-014-2279</a>
  <span class="btn-bar" style="left:240px;top:460px;height:40px"></span>
</section>

<section class="features">
  <div class="brand center-brand abs" style="left:498px;top:70px">Quorbelna<small>Solutions</small></div>
  <svg class="abs" style="left:0;top:0" width="1200" height="499">
    <path d="M414 150 Q600 330 786 150" fill="none" stroke="#cfcfcf" stroke-width="2.5"/>
  </svg>
  <div class="feat-box" style="left:380px;top:124px">
    <svg width="44" height="44" viewBox="0 0 44 44" fill="none" stroke="#fff" stroke-width="1.8"><path d="M3 16l8-6 6 4 6-3 6 3 8-4 4 6"/><path d="M6 20l10 12a3 3 0 0 0 4-1l2 1a3 3 0 0 0 4-2 3 3 0 0 0 4-2 3 3 0 0 0 3-4l-9-8"/><path d="M14 24l4 4M17 21l5 5M20 19l5 5"/></svg>
  </div>
  <div class="feat-box" style="left:755px;top:124px">
    <svg width="44" height="44" viewBox="0 0 44 44" fill="none" stroke="#fff" stroke-width="1.8"><ellipse cx="26" cy="9" rx="7" ry="3"/><path d="M19 9v8c0 1.7 3 3 7 3s7-1.3 7-3V9M19 13c0 1.7 3 3 7 3s7-1.3 7-3"/><circle cx="33" cy="20" r="4"/><path d="M4 30l7-4h8l6 3h-8M13 31l10 2 14-6-2-3-12 4M4 36l6-2 12 3"/></svg>
  </div>
  <div class="feat-box red" style="left:566px;top:225px">
    <svg width="42" height="42" viewBox="0 0 42 42" fill="none" stroke="#fff" stroke-width="1.8"><path d="M21 3l15 5v11c0 10-7 17-15 20C13 36 6 29 6 19V8z"/><path d="M21 8l10 3v8c0 7-5 12-10 14-5-2-10-7-10-14v-8z"/><circle cx="21" cy="19" r="5"/><path d="M18 23l-2 6 5-2 5 2-2-6"/></svg>
  </div>
  <div class="feat abs" style="left:120px;top:121px;width:229px;text-align:right">
    <h3>A True Partner</h3>
    <p>One size data center architecture does not fit all. We take the time to understand your specific requirements.</p>
  </div>
  <div class="feat abs" style="left:858px;top:121px;width:180px">
    <h3>Availability</h3>
    <p>The facility is powered by two separate utility feeds and a Ironvale diesel generator.</p>
  </div>
  <div class="feat abs" style="left:480px;top:314px;width:240px;text-align:center">
    <h3>High Security</h3>
    <p>Our data center is a Tier III, standalone structure designed to withstand wind speeds up to 206mph.</p>
  </div>
</section>

<div class="about-frame"></div>
<div class="about-photo" role="img" aria-label="Two colleagues working together at a desk with code on several monitors"></div>
<section class="about-copy">
  <div class="eyebrow">About</div>
  <h2 class="section-title" style="margin-top:10px">Quorbelna Solutions</h2>
  <span class="accent-rule" style="left:0;top:73px;width:80px"></span>
  <p style="margin-top:26px">Like most great businesses Quorbelna Solutions began in a gargage during the summer of 1995 in Dunhollow, SC. It was a part time venture by Darren Pelloway and his business partner Colin Vesk. They had discovered an opportunity in technology sales and service after a combined 30 years at Eastline Power in information technology.</p>
  <p>Today, the company has grown significantly and continues to do so. Quorbelna Solutions provides services including multi-dwelling unit managed networks, data center services, low voltage wiring and local office IT support. Industries served include: retail, manufacturing, MDUs, hospitality, software development, medical, construction and more.</p>
</section>
<a class="btn" href="#" style="left:615px;top:1608px;width:161px;height:40px">Read More</a>
<span class="btn-bar" style="left:781px;top:1608px;height:40px"></span>

<h2 class="section-title services-title">Our Services</h2>
<span class="accent-rule" style="left:510px;top:1796px;width:80px"></span>

<div class="svc" style="left:94px;top:1844px">
  <div class="svc-icon"><svg width="48" height="48" viewBox="0 0 48 48" fill="none" stroke="#c8262e" stroke-width="1.6"><circle cx="24" cy="24" r="13"/><rect x="18" y="23" width="12" height="9"/><path d="M20 23v-3a4 4 0 0 1 8 0v3"/><path d="M24 3v6M24 39v6M3 24h6M39 24h6M9 9l4 4M35 35l4 4M39 9l-4 4M9 39l4-4"/></svg></div>
  <h3>Managed<br>Cybersecurity</h3>
  <p>Enterprise-grade cybersecurity — without the enterprise price tag.</p>
</div>
<div class="svc" style="left:459px;top:1844px">
  <div class="svc-icon"><svg width="48" height="48" viewBox="0 0 48 48" fill="none" stroke="#c8262e" stroke-width="1.6"><circle cx="24" cy="14" r="9"/><circle cx="24" cy="14" r="3"/><path d="M6 32l8-4h10l6 3h-8M16 34l12 2 14-8-2-3-12 5M6 40l6-2 14 3"/></svg></div>
  <h3>Managed Networks<br>for MDUs</h3>
  <p>High speed internet is now the number one amenity for multi-dwelling units.</p>
</div>
<div class="svc" style="left:824px;top:1844px">
  <div class="svc-icon"><svg width="52" height="48" viewBox="0 0 52 48" fill="none" stroke="#c8262e" stroke-width="1.6"><path d="M14 18a9 9 0 0 1 17-5 7 7 0 0 1 11 6 6 6 0 0 1 0 12"/><rect x="5" y="20" width="16" height="22"/><rect x="21" y="24" width="16" height="18"/><rect x="37" y="28" width="10" height="14"/><path d="M8 25h10M8 30h10M8 35h10M24 29h10M24 34h10"/></svg></div>
  <h3>Data Center<br>Services</h3>
  <p>Quorbelna Solutions offers a full suite of data center services.</p>
</div>
<div class="svc-rule"></div>
<div class="svc" style="left:272px;top:2084px">
  <div class="svc-icon"><svg width="48" height="48" viewBox="0 0 48 48" fill="none" stroke="#c8262e" stroke-width="1.6"><rect x="6" y="10" width="14" height="30"/><path d="M10 16h6M10 22h6M10 28h6M20 26h12M20 32h18"/><circle cx="34" cy="16" r="8"/><path d="M35 11l-3 5h4l-3 5"/></svg></div>
  <h3>Low Voltage<br>Wiring</h3>
  <p>To keep everyone connected with the outside world, modern buildings</p>
</div>
<div class="svc" style="left:637px;top:2084px">
  <div class="svc-icon"><svg width="48" height="48" viewBox="0 0 48 48" fill="none" stroke="#c8262e" stroke-width="1.6"><rect x="5" y="10" width="38" height="26"/><path d="M19 36v6M29 36v6M14 42h20"/><circle cx="30" cy="20" r="5"/><path d="M30 11v4M30 25v4M21 20h4M35 20h4M10 28h14"/></svg></div>
  <h3>Office IT<br>Support</h3>
  <p>Managed security services provide comprehensive protection &amp; monitoring.</p>
</div>

<section class="contact" role="region" aria-label="Contact">
  <div class="abs" style="inset:0;background:radial-gradient(ellipse at 75% 40%,rgba(80,100,120,.3),transparent 60%)" role="img" aria-label="Dark office with people working at computer screens"></div>
  <h2 style="left:62px;top:72px">Contact Us</h2>
  <div class="contact-divider"></div>
  <div class="c-item" style="top:138px">
    <h4><svg width="20" height="20" viewBox="0 0 24 24"><path fill="#c8262e" d="M6.6 10.8a15.1 15.1 0 0 0 6.6 6.6l2.2-2.2a1 1 0 0 1 1-.25 11.4 11.4 0 0 0 3.6.57 1 1 0 0 1 1 1V20a1 1 0 0 1-1 1A17 17 0 0 1 3 4a1 1 0 0 1 1-1h3.5a1 1 0 0 1 1 1c0 1.25.2 2.45.57 3.570a1 1 0 0 1-.25 1z"/></svg>Call Us</h4>
    <p>555-014-2279.</p>
  </div>
  <div class="c-item" style="top:213px">
    <h4><svg width="20" height="16" viewBox="0 0 20 16"><rect width="20" height="16" fill="#c8262e"/><path d="M1 1l9 7 9-7M1 15l6-6M19 15l-6-6" stroke="#fff" stroke-width="1.4" fill="none"/></svg>Email</h4>
    <p>support@quorbelna.com</p>
  </div>
  <div class="c-item" style="top:292px">
    <h4><svg width="20" height="20" viewBox="0 0 24 24"><path fill="#c8262e" d="M12 2a7 7 0 0 0-7 7c0 5 7 13 7 13s7-8 7-13a7 7 0 0 0-7-7zm0 9.5A2.5 2.5 0 1 1 12 6.5a2.5 2.5 0 0 1 0 5z"/></svg>Location</h4>
    <p>Quorbelna Solutions 48 Larkmoor Road<br>Dunhollow, SC 29000</p>
  </div>
  <h2 style="left:412px;top:72px">Get In Touch</h2>
  <div class="field" style="left:419px;top:139px;width:352px;height:41px;font-weight:500">First Name</div>
  <div class="field" style="left:788px;top:139px;width:351px;height:41px">Last Name</div>
  <div class="field" style="left:419px;top:194px;width:352px;height:41px">Email</div>
  <div class="field" style="left:788px;top:194px;width:351px;height:41px">Phone Number</div>
  <div class="field" style="left:419px;top:251px;width:720px;height:82px">Message</div>
  <a class="btn" href="#" style="left:419px;top:349px;width:160px;height:40px">Send Message</a>
  <span class="btn-bar" style="left:584px;top:349px;height:40px"></span>
</section>

<footer class="footer">
  <div class="brand">Quorbelna<small>Solutions</small></div>
  <span class="social" style="left:62px" aria-label="Social profile"></span>
  <span class="social" style="left:109px" aria-label="Social profile"></span>
  <span class="social" style="left:156px" aria-label="Social profile"></span>
  <span class="social" style="left:202px" aria-label="Social profile"></span>
  <div class="f-col" style="left:335px;top:46px">
    <h4>Links</h4>
    <div style="margin-top:6px"><a href="#">Home</a><a href="#">About Us</a><a href="#">Services</a><a href="#">Contact Us</a></div>
  </div>
  <div class="f-col" style="left:609px;top:46px">
    <h4>Services</h4>
    <div style="margin-top:6px"><a href="#">Managed Cybersecurity</a><a href="#">Managed Networks For MDUs</a><a href="#">Data Center Services</a><a href="#">Low Voltage Wiring</a><a href="#">Office IT Support</a></div>
  </div>
  <div class="f-contact" style="top:41px">
    <h4 style="font-size:18px;font-weight:600">Contact Us</h4>
  </div>
  <div class="f-contact" style="top:91px">
    <span class="f-icon"><svg width="20" height="20" viewBox="0 0 24 24"><path fill="#fff" d="M6.6 10.8a15.1 15.1 0 0 0 6.6 6.6l2.2-2.2a1 1 0 0 1 1-.25 11.4 11.4 0 0 0 3.6.57 1 1 0 0 1 1 1V20a1 1 0 0 1-1 1A17 17 0 0 1 3 4a1 1 0 0 1 1-1h3.5a1 1 0 0 1 1 1c0 1.25.2 2.45.57 3.57a1 1 0 0 1-.25 1z"/></svg></span>
    <div class="f-text" style="top:-3px"><h5>Call Us</h5><p>555-014-2279.</p></div>
  </div>
  <div class="f-contact" style="top:163px">
    <span class="f-icon"><svg width="22" height="16" viewBox="0 0 22 16"><rect x="1" y="1" width="20" height="14" fill="none" stroke="#fff" stroke-width="1.6"/><path d="M1 1l10 8 10-8M1 15l7-6M21 15l-7-6" stroke="#fff" stroke-width="1.4" fill="none"/></svg></span>
    <div class="f-text" style="top:-6px"><h5>Email</h5><p>Support@quorbelna.com</p></div>
  </div>
  <div class="f-contact" style="top:235px">
    <span class="f-icon"><svg width="20" height="20" viewBox="0 0 24 24"><path fill="#fff" d="M12 2a7 7 0 0 0-7 7c0 5 7 13 7 13s7-8 7-13a7 7 0 0 0-7-7zm0 9.5A2.5 2.5 0 1 1 12 6.5a2.5 2.5 0 0 1 0 5z"/></svg></span>
    <div class="f-text" style="top:-12px"><h5>Location</h5><p>Quorbelna Solutions 48<br>Larkmoor Road<br>Dunhollow, SC 29000</p></div>
  </div>
  <div class="f-rule"></div>
  <div class="copyright">2025 © Quorbelna Solutions of SC, Inc.</div>
</footer>

</body>
</html>
```